Web site for Tree Removal Company

What we are looking for:
-------------------------------
Looking for a wordpress web site, you can provide your own template or we can supply you with one (http://pelorin.vextura.com).

What we do
---------------
To see what we do please go to google Australia and google "Tree removal Sydney" or "Tree Removal Melbourne".

Web site requirements
-----------------------------
We prefer you to use our template as it has all our requirements in already.
- Responsive.
- Based on Wordpress.
- Full complaint and compatible with plugs.

Look, Feel and Appearance
------------------------------------
Please use the logo (see attached), for colour scheme, look and feel of the web site.

Thank you for your time and effort!

Target Market(s)

Tree Removal for Residential Homes

Industry/Entity Type

It Company

Number of Pages Required

4 page

Font styles to use
Serif
Sans Serif

Requirements
Must have
• Wordpress
Nice to have
• Original artwork, images and text
Should not have
• non related images or wording

```html
<!DOCTYPE html>
<html lang="en">
<head>
<meta charset="utf-8">
<title>Arbor Kin — Tree Removal</title>
<link href="https://fonts.googleapis.com/css2?family=Jost:wght@400;500&family=Open+Sans:wght@400;600;700&display=swap" rel="stylesheet">
<style>
:root{
  --accent:#1ec2ea;
  --ink:#333;
  --muted:#555;
  --paper:#f4f4f3;
  --white:#fff;
  --night:#2b2b2b;
  --night-soft:#3a3a3a;
  --rule:#888;
}
*{box-sizing:border-box;margin:0;padding:0}
html,body{width:1200px;height:3280px;overflow:hidden}
body{font-family:"Open Sans",Arial,sans-serif;color:var(--ink);background:var(--paper);position:relative}
.heading{font-family:"Jost",Helvetica,sans-serif;font-weight:400;font-size:40px;color:var(--ink);text-align:center}
.heading-rule{width:70px;height:2px;background:var(--rule);margin:26px auto 0}
.copy{font-size:15px;line-height:30px;color:var(--muted);text-align:center}
.btn{display:inline-block;background:var(--accent);color:var(--white);font-family:"Open Sans",Arial,sans-serif;font-weight:600;border-radius:2px;text-align:center}

/* header + hero */
.hero{position:absolute;left:0;top:0;width:1200px;height:656px;background:linear-gradient(135deg,#6b5a2a 0%,#8d7a3c 30%,#5a4f2a 55%,#7a5d2f 80%,#4b3b22 100%)}
.site-header{position:absolute;left:0;top:0;width:1200px;height:123px;background:rgba(20,20,20,.72);z-index:2}
.brand{position:absolute;left:82px;top:30px;display:flex;align-items:center;gap:12px}
.brand-dot{width:44px;height:44px;border-radius:50%;background:var(--accent)}
.brand-name{font-family:"Open Sans",Arial,sans-serif;font-weight:600;font-size:18px;color:var(--white);letter-spacing:1px}
.main-nav{position:absolute;right:42px;top:48px;display:flex;gap:14px}
.main-nav a{font-size:15px;font-weight:600;color:var(--white);text-decoration:none;padding:4px 14px;border-radius:2px}
.main-nav a.is-current{background:var(--accent)}
.hero-caption{position:absolute;left:555px;top:328px;width:645px;height:232px;background:rgba(15,15,15,.82);padding:26px 32px}
.hero-title{font-family:"Jost",Helvetica,sans-serif;font-size:30px;color:var(--white);letter-spacing:1px}
.hero-text{font-size:14px;line-height:24px;color:#ddd;margin-top:12px;width:500px}
.hero-caption .btn{margin-top:20px;font-size:16px;padding:9px 20px}

/* welcome */
.welcome{position:absolute;left:0;top:656px;width:1200px;height:500px}
.welcome .heading{margin-top:56px}
.welcome .copy{width:980px;margin:34px auto 0}
.welcome .btn{position:absolute;left:390px;top:382px;width:410px;height:40px;line-height:40px;font-size:16px}

/* what we do */
.what{position:absolute;left:0;top:1156px;width:1200px;height:498px}
.what .heading{margin-top:38px}
.what .copy{width:900px;margin:34px auto 0}
.what-art{position:absolute;left:328px;top:252px;width:520px;height:246px;border-radius:4px;background:linear-gradient(90deg,#b45a3c 0%,#5c6a86 18%,#e0b220 45%,#d9c9a4 75%,#c9c2b3 100%)}

/* services */
.services{position:absolute;left:0;top:1654px;width:1200px;height:292px;background:var(--white);box-shadow:0 10px 20px rgba(0,0,0,.08)}
.service{position:absolute;top:98px;width:320px}
.service-icon{position:absolute;left:0;top:0;width:54px;height:54px;border:1px solid #ddd;background:var(--white)}
.service-body{margin-left:92px}
.service-title{font-family:"Jost",Helvetica,sans-serif;font-size:21px;font-weight:500;color:var(--ink)}
.service-title.is-active{color:var(--accent)}
.service-text{font-size:14px;line-height:26px;color:var(--muted);margin-top:10px}
.service-more{display:inline-block;font-size:12px;color:#777;text-decoration:underline;margin-top:18px}

/* monthly special */
.special{position:absolute;left:0;top:1946px;width:1200px;height:399px}
.special .heading{margin-top:84px}
.special .copy{width:1000px;margin:34px auto 0}
.special .btn{position:absolute;left:544px;top:292px;width:131px;height:40px;line-height:40px;font-size:19px}

/* why choose */
.why{position:absolute;left:0;top:2345px;width:1200px;height:456px;background:linear-gradient(180deg,#2d3433 0%,#4a5248 40%,#3c4436 70%,#2f3530 100%)}
.why .heading{color:var(--white);margin-top:46px;font-size:38px}
.why .heading-rule{background:#ccc;margin-top:20px}
.why .copy{color:#eee;margin-top:30px}
.reason{position:absolute;top:248px;width:200px;text-align:center}
.reason-icon{width:76px;height:76px;margin:0 auto;border:2px solid var(--white);border-radius:50%;display:flex;align-items:center;justify-content:center}
.reason-icon.is-active{border-color:var(--accent)}
.reason-label{font-family:"Jost",Helvetica,sans-serif;font-size:22px;color:var(--white);margin-top:34px}
.reason-label.is-active{color:var(--accent)}

/* partners */
.partners{position:absolute;left:0;top:2801px;width:1200px;height:164px;background:var(--white)}
.partner-arrow{position:absolute;top:70px}
.partner{position:absolute;top:52px;background:#e3e6e0}
.partner.round{width:58px;height:58px;border-radius:50%;background:#2f7a3a}
.partner.wide{height:30px;top:66px;width:170px;background:#d8dcc6}

/* footer */
.site-footer{position:absolute;left:0;top:2965px;width:1200px;height:315px;background:var(--night)}
.footer-title{font-size:15px;color:var(--white);font-weight:600}
.footer-nav{position:absolute;left:142px;top:44px}
.footer-nav ul{list-style:none;margin-top:22px}
.footer-nav li{font-size:14px;color:var(--white);line-height:36px;padding-left:22px;position:relative}
.footer-nav li::before{content:"";position:absolute;left:2px;top:16px;width:5px;height:5px;background:#ccc;border-radius:50%}
.footer-nav li.is-current{color:var(--accent)}
.footer-nav li.is-current::before{background:var(--accent)}
.quick-contact{position:absolute;left:451px;top:44px;width:280px}
.field{height:34px;margin-top:8px;background:var(--night-soft);border:1px solid #444;font-size:12px;color:var(--white);padding:9px 10px;position:relative}
.quick-contact .field:first-of-type{margin-top:22px}
.field.tall{height:42px}
.field-caret{position:absolute;right:12px;top:10px}
.send{position:absolute;right:0;bottom:-42px;width:44px;height:24px;line-height:24px;font-size:11px;font-weight:600}
.footer-brand{position:absolute;left:930px;top:40px;width:180px;text-align:center}
.footer-brand .brand-dot{margin:0 auto}
.footer-brand .brand-name{margin-top:10px}
.footer-brand-rule{width:140px;height:1px;background:#555;margin:16px auto 0}
.social{display:flex;gap:14px;justify-content:center;margin-top:18px}
.social span{width:30px;height:30px;border-radius:50%;background:#555}
.social span.is-active{background:var(--accent)}
.copyright{font-size:13px;color:#ddd;margin-top:18px}
</style>
</head>
<body>

<section class="hero" role="img" aria-label="Photo of an arborist in safety gear cutting a felled tree with a chainsaw in autumn woodland"></section>

<header class="site-header">
  <div class="brand"><span class="brand-dot"></span><span class="brand-name">ARBOR KIN</span></div>
  <nav class="main-nav">
    <a class="is-current">Home</a><a>About Us</a><a>Services</a><a>Contact Us</a>
  </nav>
</header>

<div class="hero-caption">
  <h1 class="hero-title">Any Tree Any Place</h1>
  <p class="hero-text">Lorem ipsum dolor sit amet, couer adipscing elit. Praesent vestibuluolestie lacus. Aenean nonummy hendrerit mauris.</p>
  <span class="btn">Free Online Quote</span>
</div>

<section class="welcome">
  <h2 class="heading">Welcome to Arbor Kin</h2>
  <div class="heading-rule"></div>
  <p class="copy">Lorem ipsum dolor sit amet, couer adipscing elit. Praesent vestibuluolestie lacus. Aenean nonummy hendrerit mauris. Lorem ipsum dolor sit amet, couer adipscing elit. Praesent vestibuluolestie lacus. Aenean nonummy hendrerit mauris. Lorem ipsum dolor sit amet, couer adipscing elit. Praesent vestibuluolestie lacus. Aenean nonummy hendrerit mauris. Lorem ipsum dolor sit amet, couer adipscing elit. Praesent vestibuluolestie lacus. Aenean nonummy hendrerit mauris. Lorem ipsum dolor sit amet, couer adipscing elit. Praesent vestibuluolestie lacus. Aenean nonummy hendrerit mauris. Lorem ipsum dolor sit amet, couer adipscing elit. Praesent vestibuluolestie lacus. Aenean nonummy hendrerit mauris.</p>
  <span class="btn">Get FREE quotes from tree removal experts</span>
</section>

<section class="what">
  <h2 class="heading">What we do</h2>
  <div class="heading-rule"></div>
  <p class="copy">Lorem ipsum dolor sit amet, couer adipscing elit. Praesent vestibuluolestie lacus. Aenean nonummy hendrerit mauris.<br>Lorem ipsum dolor sit amet, couer adipscing elit.</p>
  <div class="what-art" role="img" aria-label="Illustration of a lumberjack holding an axe beside a yellow log truck loaded with timber"></div>
</section>

<section class="services">
  <div class="service" style="left:112px">
    <span class="service-icon"><svg width="54" height="54" viewBox="0 0 54 54"><path d="M17 36 L17 18 L27 18 Q34 18 34 24 Q34 30 27 30 L17 30 M26 30 L36 38" fill="none" stroke="#1ec2ea" stroke-width="2"/></svg></span>
    <div class="service-body">
      <h3 class="service-title is-active">Tree Removal</h3>
      <p class="service-text">Lorem ipsum dolor sit amet, couer adipscing elit. Praesent vestibuluolestie</p>
      <a class="service-more">read more</a>
    </div>
  </div>
  <div class="service" style="left:470px">
    <span class="service-icon" style="border:none"><svg width="54" height="54" viewBox="0 0 54 54"><rect x="14" y="22" width="26" height="14" fill="#222"/><rect x="10" y="34" width="34" height="4" fill="#222"/></svg></span>
    <div class="service-body">
      <h3 class="service-title">Stump Grinding</h3>
      <p class="service-text">Lorem ipsum dolor sit amet, couer adipscing elit. Praesent vestibuluolestie</p>
      <a class="service-more">read more</a>
    </div>
  </div>
  <div class="service" style="left:828px">
    <span class="service-icon"><svg width="54" height="54" viewBox="0 0 54 54"><circle cx="27" cy="23" r="10" fill="none" stroke="#333" stroke-width="2"/><line x1="27" y1="33" x2="27" y2="42" stroke="#333" stroke-width="2"/></svg></span>
    <div class="service-body">
      <h3 class="service-title">Tree Pruning</h3>
      <p class="service-text">Lorem ipsum dolor sit amet, couer adipscing elit. Praesent vestibuluolestie</p>
      <a class="service-more">read more</a>
    </div>
  </div>
</section>

<section class="special">
  <h2 class="heading">Monthly Special</h2>
  <div class="heading-rule"></div>
  <p class="copy">Lorem ipsum dolor sit amet, couer adipscing elit. Praesent vestibuluolestie lacus. Aenean nonummy hendrerit mauris.<br>Lorem ipsum dolor sit amet, couer adipscing elit.</p>
  <span class="btn">Join now</span>
</section>

<section class="why" role="img" aria-label="Dimmed photo of a tree-lined suburban street behind the section">
  <h2 class="heading">Why choose Arbor Kin Services?</h2>
  <div class="heading-rule"></div>
  <p class="copy">Lorem ipsum dolor sit amet, couer adipscing elit. Praesent vestibuluolestie lacus.</p>
  <div class="reason" style="left:151px">
    <div class="reason-icon is-active"><svg width="36" height="36" viewBox="0 0 36 36"><path d="M8 19 L15 26 L29 11" fill="none" stroke="#1ec2ea" stroke-width="3"/></svg></div>
    <div class="reason-label is-active">Truthful</div>
  </div>
  <div class="reason" style="left:365px">
    <div class="reason-icon"><svg width="36" height="36" viewBox="0 0 36 36"><circle cx="18" cy="14" r="8" fill="#fff"/><path d="M12 20 L10 32 L18 28 L26 32 L24 20" fill="#fff"/></svg></div>
    <div class="reason-label">Reputable</div>
  </div>
  <div class="reason" style="left:605px">
    <div class="reason-icon"><svg width="36" height="36" viewBox="0 0 36 36"><circle cx="18" cy="12" r="6" fill="#fff"/><path d="M7 30 Q7 20 18 20 Q29 20 29 30 Z" fill="#fff"/></svg></div>
    <div class="reason-label">Highly Professional</div>
  </div>
  <div class="reason" style="left:854px">
    <div class="reason-icon"><svg width="36" height="36" viewBox="0 0 36 36"><rect x="9" y="9" width="18" height="18" fill="#fff"/><rect x="14" y="14" width="8" height="8" fill="#3c4436"/></svg></div>
    <div class="reason-label">Best Value</div>
  </div>
</section>

<section class="partners">
  <svg class="partner-arrow" style="left:52px" width="16" height="24" viewBox="0 0 16 24"><path d="M12 3 L4 12 L12 21" fill="none" stroke="#222" stroke-width="3"/></svg>
  <span class="partner round" style="left:102px"></span>
  <span class="partner wide" style="left:226px"></span>
  <span class="partner wide" style="left:486px;width:170px;background:#ddd"></span>
  <span class="partner" style="left:728px;top:50px;width:66px;height:62px;background:#e4e4e4"></span>
  <span class="partner round" style="left:880px"></span>
  <span class="partner wide" style="left:1016px;width:80px"></span>
  <svg class="partner-arrow" style="left:1134px" width="16" height="24" viewBox="0 0 16 24"><path d="M4 3 L12 12 L4 21" fill="none" stroke="#222" stroke-width="3"/></svg>
</section>

<footer class="site-footer">
  <nav class="footer-nav">
    <div class="footer-title">Navigation links</div>
    <ul>
      <li class="is-current">Home</li><li>About Us</li><li>Services</li><li>Contact Us</li>
    </ul>
  </nav>
  <div class="quick-contact">
    <div class="footer-title">Quick Contact</div>
    <div class="field">Name</div>
    <div class="field">Email</div>
    <div class="field">Services<svg class="field-caret" width="12" height="10" viewBox="0 0 12 10"><path d="M1 2 L6 8 L11 2" fill="none" stroke="#ccc" stroke-width="1.5"/></svg></div>
    <div class="field tall">message</div>
    <span class="btn send">SEND</span>
  </div>
  <div class="footer-brand">
    <span class="brand-dot" style="display:block"></span>
    <div class="brand-name">ARBOR KIN</div>
    <div class="footer-brand-rule"></div>
    <div class="social"><span></span><span class="is-active"></span><span></span></div>
    <p class="copyright">Copyright © Arbor Kin</p>
  </div>
</footer>

</body>
</html>
```